Stride Ledger Booklet

I have a 25 page booklet that I wrote.
I need to have a book cover design, typesetting, and imagery.
I need it to be designed with bleeds because I am having it printed.
It will be in an 8.5 X 11 format.
Please look at the 2020*.png files for an idea for the cover.
The title of the mini-book is "Stride Ledger" .
Subtitle is "Kelvaro Method for Health and Fitness Motivation"
Then in between the title and subtitle, place the "Dwayne_Health_Infographic...." image.
The other images are for inside the mini-book,
The "Stride-Ledger-KelvarO.pdf" file is the information in the book that will need to be typesetted.
The other images are inside the book and will need to be placed inside when appropriate.
Please don't agree to do this project if you have not done this before
I also want to see your portfolio.
Thank you
P.S. I can add all my images that are in the booklet when you accept project

Target Market(s)

Baby boomers ages 50-70

Industry/Entity Type

Fitness

Colors
0a5aa6

Requirements
Must have
• My project consists of a book cover and back. And typesetting and imagery inside the book.

```html
<!DOCTYPE html>
<html lang="en">
<head>
<meta charset="utf-8">
<title>Stride Ledger Booklet</title>
<link href="https://fonts.googleapis.com/css2?family=Roboto+Condensed:wght@400;700&family=Source+Sans+3:wght@300;400;600;700&display=swap" rel="stylesheet">
<style>
:root{
  --brand-blue:#0a5aa6;
  --deep-blue:#0d4fb0;
  --accent-red:#e3120b;
  --backdrop:#d9d9d9;
  --paper:#ffffff;
  --ink:#333333;
  --muted:#555555;
  --pale-blue:#e6eef8;
}
*{margin:0;padding:0;box-sizing:border-box}
html,body{width:1200px;height:1100px;overflow:hidden;background:var(--backdrop)}
body{position:relative;font-family:"Source Sans 3",Arial,sans-serif;color:var(--ink)}
.page{position:absolute;width:320px;height:414px;background:var(--paper);overflow:hidden;box-shadow:0 4px 12px rgba(0,0,0,.28)}
.page--front{left:70px;top:102px;background:var(--deep-blue)}
.page--title{left:423px;top:102px}
.page--back{left:779px;top:102px}
.page--forward{left:70px;top:556px}
.page--purpose{left:423px;top:556px}
.cover-art{position:absolute;left:0;top:0;width:320px;height:414px}
.cover-title{position:absolute;left:110px;top:30px;font-family:"Roboto Condensed",Arial,sans-serif;font-weight:700;font-size:38px;line-height:42px;letter-spacing:.3px}
.page--front .cover-title{color:#fff}
.page--title .cover-title{color:var(--deep-blue);left:116px;top:32px}
.cover-subtitle{position:absolute;left:110px;top:124px;width:210px;font-weight:300;font-size:12.5px;line-height:15px}
.page--front .cover-subtitle{color:#e8eefa}
.page--title .cover-subtitle{color:#111;left:116px;top:120px}
.brand-name{position:absolute;right:30px;top:366px;font-family:"Roboto Condensed",Arial,sans-serif;font-weight:700;font-size:17px;letter-spacing:1px}
.page--front .brand-name{color:#fff}
.page--title .brand-name{color:#111;top:369px}
.back-band{position:absolute;left:0;top:140px;width:320px;height:94px;background:var(--deep-blue);color:#fff;text-align:center;font-size:6.6px;line-height:13px;padding-top:14px}
.back-band strong{font-weight:700}
.sheet-body{position:absolute;left:31px;top:24px;width:258px;font-size:4.6px;line-height:6.3px;color:var(--ink)}
.sheet-body p{margin-bottom:6px}
.sheet-body h3{font-size:7.4px;line-height:9px;font-weight:400;color:var(--muted);margin:9px 0 6px}
.sheet-body h3:first-child{margin-top:6px}
.bio-block{position:relative;min-height:124px;margin-bottom:2px}
.bio-block p{width:150px}
.portrait{position:absolute;left:146px;top:-16px;width:130px;height:130px}
.sheet-body .lead-list{color:var(--deep-blue);list-style:none;margin-bottom:6px}
.sheet-footer{position:absolute;left:0;top:396px;width:320px;height:8px;background:var(--deep-blue);color:#fff;font-size:3.8px;line-height:8px}
.sheet-footer .copyright{position:absolute;left:31px}
.sheet-footer .web{position:absolute;left:175px}
.sheet-footer .footer-brand{position:absolute;left:228px;top:-2px;width:50px;height:12px;background:var(--paper);color:#111;font-family:"Roboto Condensed",Arial,sans-serif;font-weight:700;font-size:7px;line-height:12px;text-align:center}
.sheet-footer .folio{position:absolute;left:299px}
.section-title{position:absolute;left:32px;top:20px;width:256px;border-top:3px double var(--deep-blue);border-bottom:3px double var(--deep-blue);text-align:center;font-family:"Roboto Condensed",Arial,sans-serif;font-weight:700;font-size:13px;line-height:20px;color:var(--deep-blue)}
.page--purpose .sheet-body{left:32px;top:54px;width:256px}
</style>
</head>
<body>

<section class="page page--front">
  <svg class="cover-art" viewBox="0 0 320 414">
    <defs>
      <linearGradient id="photoCool" x1="0" y1="0" x2="1" y2="1"><stop offset="0" stop-color="#7d8c99"/><stop offset="1" stop-color="#3e4c5a"/></linearGradient>
      <linearGradient id="photoWarm" x1="0" y1="0" x2="1" y2="1"><stop offset="0" stop-color="#9a7b66"/><stop offset="1" stop-color="#3b3a40"/></linearGradient>
      <linearGradient id="photoGym" x1="0" y1="0" x2="1" y2="1"><stop offset="0" stop-color="#cfd6de"/><stop offset="1" stop-color="#5b6e86"/></linearGradient>
    </defs>
    <polygon points="0,245 40,285 0,325" fill="var(--accent-red)"/>
    <polygon points="78,414 108,384 138,414" fill="var(--accent-red)"/>
    <polygon points="64,136 130,202 64,268 -2,202" fill="url(#photoCool)" role="img" aria-label="Photo of an athlete running on a treadmill"/>
    <polygon points="112,240 162,290 112,340 62,290" fill="url(#photoWarm)" role="img" aria-label="Photo of a man training shirtless in a gym"/>
    <polygon points="50,308 112,370 50,432 -12,370" fill="url(#photoGym)" role="img" aria-label="Photo of running shoes on a treadmill belt"/>
  </svg>
  <h1 class="cover-title">STRIDE<br>LEDGER</h1>
  <p class="cover-subtitle">Kelvaro Method for Health and<br>Fitness Motivation</p>
  <div class="brand-name">KELVARO</div>
</section>

<section class="page page--title">
  <svg class="cover-art" viewBox="0 0 320 414">
    <polygon points="0,245 40,285 0,325" fill="var(--deep-blue)"/>
    <polygon points="78,414 108,384 138,414" fill="var(--deep-blue)"/>
    <polygon points="64,136 130,202 64,268 -2,202" fill="url(#photoCool)" role="img" aria-label="Photo of an athlete running on a treadmill"/>
    <polygon points="112,240 162,290 112,340 62,290" fill="url(#photoWarm)" role="img" aria-label="Photo of a man training shirtless in a gym"/>
    <polygon points="50,308 112,370 50,432 -12,370" fill="url(#photoGym)" role="img" aria-label="Photo of running shoes on a treadmill belt"/>
  </svg>
  <h1 class="cover-title">STRIDE<br>LEDGER</h1>
  <p class="cover-subtitle">Kelvaro Method for Health and<br>Fitness Motivation</p>
  <div class="brand-name">KELVARO</div>
</section>

<section class="page page--back">
  <div class="back-band">
    Finally...How You Can Finally Achieve an Elite Level of<br>
    Fitness...Even if You are Starting at the Age of 63...like I did!<br>
    Watch Your Fitness Soar with the Newly Revealed “Kelvaro<br>
    Method” that Transforms you from<br>
    <strong>“Exerciser” to “Athlete”</strong>
  </div>
</section>

<section class="page page--forward">
  <div class="sheet-body">
    <h3>Forward</h3>
    <p>This manifesto could change your life. I know it seems rather bold to claim that you can sit down for the next few minutes and read something that could alter the course of your life. In fact, I wouldn't have believed it myself just a few short years ago.</p>
    <p>But three years ago, at the age of sixty-three, I started on a journey that would change my life forever. What you are reading right now is the result of three years of experimentation, reading, watching, testing, and taking ACTION that has allowed me to achieve a high degree of fitness and health in my sixties.</p>
    <p>This manifesto is going to upset the “apple cart” big time. A lot of fitness trainers, local gyms, and companies in the health and fitness industry are going to be very pissed at me.</p>
    <p><strong>But what I've learned is too powerful to keep to myself, so I just had to share it with you.</strong></p>
    <p>Before we get started, spend a few moments studying the cover page of this document. It may feel a little overwhelming, but I promise you'll understand it when you finish this manifesto.</p>
    <p>As you read, my hope is that you will begin to see the “Big Takeaway.” This takeaway has changed my life. And my hope and dream is that it does the same for you.</p>
    <h3>Who is Dwayne Hollis</h3>
    <div class="bio-block">
      <svg class="portrait" viewBox="0 0 130 130">
        <circle cx="72" cy="72" r="55" fill="var(--deep-blue)"/>
        <circle cx="62" cy="62" r="54" fill="#fff"/>
        <circle cx="62" cy="62" r="51" fill="#8a7a6e" role="img" aria-label="Photo of the author relaxing on a couch in a floral shirt"/>
      </svg>
      <p>First of all, I'm not the famous actor. If you did a Searchly search on “Dwayne Hollis,” you'd get two or three pages of the Hollywood star. I'm certainly not a star and have no ambition to be one. My story isn't made in Hollywood.</p>
      <p>Four years ago, after thirty-two years of marriage, my sixty-two-year-old wife suddenly died of a brain aneurysm while we were watching the College Football Championship game on TV. It was so fast and incredibly devastating. Unless you've experienced it, you don't understand how quickly those we love can be gone.</p>
      <p>If it hadn't been for my children and family, I would have gone into a much deeper depression than I did.</p>
      <p>Yet I did what many of us would do. I attempted to find relief in TV, food, and alcohol. As you may know, it's very easy to put on weight when you are inactive and over sixty.</p>
    </div>
    <p>To this day, I don't recall who took this picture of me. But I'm eternally grateful for the wake-up call!</p>
    <p>I feel awkward when I start to discuss this (and I mention it only because it's urgent that you begin to understand how powerful the methods I'm going to reveal to you are), but my transformation— starting at the age of sixty-three—is quite amazing according to friends, family, and even strangers.</p>
    <p>I'll show you current pictures later. And I'm doing that for a reason. This manifesto is about you, not me. This manifesto was written for YOU! You are the hero in this story.</p>
  </div>
  <footer class="sheet-footer">
    <span class="copyright">© 2019 Northgate Press Group LLC</span>
    <span class="web">www.kelvaro.com</span>
    <span class="footer-brand">KELVARO</span>
    <span class="folio">1</span>
  </footer>
</section>

<section class="page page--purpose">
  <h2 class="section-title">Purpose of Stride Ledger</h2>
  <div class="sheet-body">
    <p>To provide a proven system, for young and old alike, that gives the single-minded, competition-driven athlete a way to more energy, more muscle, less stress, better health, and victory in competition, all while committing to a simple health and fitness regimen.</p>
    <h3>Why Am I Sharing These Secrets with You?</h3>
    <p>I've already mentioned that I started this discovery a little over three years ago. There was no way I could continue on the destructive path I found myself on. I wasn't providing anything to my family but a depressed, lazy, fat man. I initially went into this discovery with the sole purpose of helping myself. What I didn't tell you is that everything I've learned and put into practice has all been for a higher purpose: I eventually realized that this needs to be shared!</p>
    <ul class="lead-list">
      <li>• A vision of a health and fitness system that could stand up on its own.</li>
      <li>• A fitness system that didn't need me.</li>
      <li>• A fitness system that was simple and still provided you with more energy, more muscle, less stress, better health, and a competitive edge!</li>
    </ul>
    <p>I'm still working on myself. I still need to tone my mid-section a little more.</p>
    <p>But my commitment to fitness excellence will never stop. I see that as my reward and motivation: <em>constant and never-ending improvement</em>.</p>
    <h3>The Reasons Most People Fail at Fitness and Health</h3>
    <p>Take a trip to your local gym. When you arrive, look around. It's always great to see people that are trying to improve their health, isn't it?</p>
    <p>But nine out of ten of them are working out ALL WRONG! They are standing around. Taking too many breaks. Texting.</p>
    <p>If you take a tour of the facility, I'll wager you'll find somebody on a stationary bike watching a movie or playing a game on his or her phone!</p>
    <p><strong>Is somebody making them be there?</strong><br>A lot of people are performing what really are (to me) ridiculous and absolutely unnecessary exercises. It almost looks like they are training just to perform tricks on a stage.</p>
    <p>And the fitness trainers . . . OUCH!</p>
    <p>It seems like they sometimes make up these funky exercises to justify their jobs. And they OVERCOMPLICATE the training so they become a crutch to the client! (Oh, boy . . . I just pissed off a bunch of fitness trainers.)</p>
    <p>And don't get me going on all these diets for fitness. Paleo! Keto! Coastline! Lowcarb Plus! They are too hard to maintain, too disruptive, and overcomplicated. Right?</p>
  </div>
  <footer class="sheet-footer">
    <span class="copyright">© 2019 Northgate Press Group LLC</span>
    <span class="web">www.kelvaro.com</span>
    <span class="footer-brand">KELVARO</span>
    <span class="folio">2</span>
  </footer>
</section>

</body>
</html>
```